BRAVEL

I NEED A DESIGN FOR THE COVER OF A CATALOG. ON THE COVER SHOULD APPEAR A FIGURE LIKE THAT OF THE EXAMPLE ATTACHED. USE THE INTENSIVE BLUE, GREEN AND FUXIA COLORS. IN ADDITION, YOU MUST ENTER THE TEXT "CALVENTA STYLE - AUTUMN - WINTER 2018-19". DESIGN THAT TRANSMIT THE IDEA OF HIGH QUALITY AND LUXURY. --------------------------------- I NEED A DESIGN FOR A CATALOG COVER. ON THE COVER, I'D LIKE TO HAVE A MODEL IN THE SAME STYLE AS THE ATTACHED SAMPLE. PLEASE USE COLORS DEEP BLUE, GREEN AND FUSCIA. ALSO, PLEASE INCORPORATE THE TEXT "CALVENTA STYLE - AUTUMN - WINTER 2018-19". THE DESIGN NEEDS TO COMMUNICATE A SENSE OF HIGH QUALITY AND LUXURY.

Target Market(s)

SALE OF FABRICS BY CATALOG

Colors
0355a3
e34197
00a990

Requirements
Must have
• AN EXCELLENT DRAWING / DESIGN

```html
<!DOCTYPE html>
<html lang="es">
<head>
<meta charset="utf-8">
<title>Calventa Style – Otoño Invierno 2018·2019</title>
<link rel="stylesheet" href="https://fonts.googleapis.com/css2?family=Antonio:wght@100&family=Cinzel:wght@400;700;900&family=Michroma&display=swap">
<style>
  :root {
    --bg: #000000;
    --fuchsia: #e6306e;
    --teal: #00a990;
    --deep-blue: #0355a3;
    --grey: #8a8a8a;
    --silver: #d9d9d9;
    --form: #2b2b2b;
    --rule: #9a9a9a;
    --ornament: #5a5a5a;
  }
  html, body {
    margin: 0;
    padding: 0;
    width: 928px;
    height: 1200px;
    overflow: hidden;
    background: var(--bg);
  }
  .cover {
    position: relative;
    width: 928px;
    height: 1200px;
    background: var(--bg);
  }
  .brand {
    position: absolute;
    left: 104px;
    width: 736px;
    top: 150px;
    height: 150px;
    display: flex;
    align-items: center;
    justify-content: center;
    gap: 22px;
  }
  .brand-mark {
    width: 78px;
    height: 78px;
    border-radius: 50%;
    background: var(--teal);
    flex: none;
  }
  .brand-name {
    margin: 0;
    font-family: "Cinzel", serif;
    font-weight: 900;
    font-size: 104px;
    line-height: 1;
    letter-spacing: -2px;
    color: var(--fuchsia);
  }
  .rule {
    position: absolute;
    height: 0;
    border-top: 1.5px dashed var(--rule);
  }
  .rule--brand { left: 104px; width: 736px; top: 338px; border-top-color: var(--deep-blue); border-top-width: 2px; }
  .rule--season { left: 282px; width: 484px; top: 766px; }
  .brand-sub {
    position: absolute;
    left: 104px;
    width: 736px;
    top: 350px;
    margin: 0;
    text-align: center;
    font-family: "Cinzel", serif;
    font-weight: 400;
    font-size: 90px;
    line-height: 1;
    color: var(--grey);
  }
  .dress-form {
    position: absolute;
    left: 104px;
    top: 410px;
    width: 162px;
    height: 694px;
  }
  .ornament-row {
    position: absolute;
    left: 282px;
    width: 484px;
    height: 22px;
    background: var(--ornament);
  }
  .ornament-row--top { top: 593px; }
  .ornament-row--mid { top: 907px; }
  .ornament-row--bottom { top: 1027px; }
  .season {
    position: absolute;
    left: 282px;
    width: 484px;
    height: 80px;
    margin: 0;
    text-align: center;
    font-family: "Antonio", sans-serif;
    font-weight: 100;
    font-size: 80px;
    line-height: 80px;
    color: var(--grey);
    transform: scaleY(1.3);
    transform-origin: center;
  }
  .season--autumn { top: 664px; }
  .season--winter { top: 778px; }
  .years {
    position: absolute;
    left: 282px;
    width: 484px;
    top: 958px;
    margin: 0;
    padding-left: 24px;
    box-sizing: border-box;
    text-align: center;
    font-family: "Michroma", sans-serif;
    font-size: 28px;
    line-height: 1;
    letter-spacing: 24px;
    color: var(--silver);
  }
</style>
</head>
<body>
  <main class="cover">
    <div class="brand">
      <h1 class="brand-name">CALVENTA</h1>
      <span class="brand-mark"></span>
    </div>
    <div class="rule rule--brand"></div>
    <p class="brand-sub">STYLE</p>

    <svg class="dress-form" viewBox="0 0 162 694" role="img" aria-label="Silhouette of a tailor's dress form on a stand">
      <rect width="162" height="694" fill="var(--form)"/>
    </svg>

    <div class="ornament-row ornament-row--top" role="img" aria-label="Row of stitched cross ornaments"></div>
    <p class="season season--autumn">OTOÑO</p>
    <div class="rule rule--season"></div>
    <p class="season season--winter">INVIERNO</p>
    <div class="ornament-row ornament-row--mid" role="img" aria-label="Row of stitched cross ornaments"></div>
    <p class="years">2018•2019</p>
    <div class="ornament-row ornament-row--bottom" role="img" aria-label="Row of stitched cross ornaments"></div>
  </main>
</body>
</html>
```